Dental Business Card

I need Dental oriented business cards.
On the front side -
- on the first line, my name:
Dr Marlo Vintner
- on the second line (just underneath):
Doctor of Dental Medicine
- on the third line, or underneath that or in a corner, I would like the address and phone number:
5182 Ch. Birchfield
Montreal QC H2T 4B9
514-629-5074
- other than that i would maybe like a logo of a tooth, but i want it to be subtle and very basic!
- I would like the card to be preferably black or dark grey-ish with the writing in white
On the other side -
- 2-3 lines with the possibility to write the next appointment the box with the lines should be white, with the rest of the card being black

```html
<!DOCTYPE html>
<html lang="en">
<head>
<meta charset="utf-8">
<title>Dr Marlo Vintner – Business Card</title>
<link href="https://fonts.googleapis.com/css2?family=Open+Sans:wght@400;600&display=swap" rel="stylesheet">
<style>
  :root {
    --page: #ececec;
    --card: #050505;
    --card-glow: #262626;
    --ink: #ffffff;
    --ink-soft: #d6d6d6;
    --ink-faint: #4a4a4a;
    --slip: #ffffff;
    --slip-rule: #2a2a2a;
  }
  * { margin: 0; padding: 0; box-sizing: border-box; }
  html, body { width: 1200px; height: 800px; overflow: hidden; }
  body {
    background: var(--page);
    font-family: "Open Sans", sans-serif;
    color: var(--ink);
    display: flex;
    align-items: center;
    justify-content: center;
    gap: 60px;
  }
  .card {
    position: relative;
    width: 520px;
    height: 297px;
    background: var(--card);
    border-radius: 4px;
    overflow: hidden;
    box-shadow: 0 10px 24px rgba(0,0,0,0.18);
  }
  .card--front {
    background: radial-gradient(ellipse at 45% 30%, var(--card-glow) 0%, var(--card) 60%);
  }
  .swirl-art {
    position: absolute;
    left: -40px;
    bottom: -60px;
    width: 260px;
    height: 200px;
    border-radius: 50%;
    background: radial-gradient(ellipse at center, rgba(70,70,70,0.35) 0%, rgba(0,0,0,0) 70%);
  }
  .brand {
    position: absolute;
    left: 34px;
    top: 40px;
    display: flex;
    align-items: center;
    gap: 8px;
    font-size: 13px;
    font-weight: 400;
    color: var(--ink-soft);
    letter-spacing: 0.04em;
  }
  .brand__dot {
    width: 14px; height: 14px;
    border: 1.5px solid var(--ink-soft);
    border-radius: 50%;
  }
  .identity {
    position: absolute;
    left: 34px;
    top: 104px;
  }
  .identity__name {
    font-size: 25px;
    font-weight: 600;
    letter-spacing: 0.01em;
    text-transform: uppercase;
  }
  .identity__title {
    margin-top: 4px;
    font-size: 16px;
    font-weight: 400;
  }
  .divider {
    position: absolute;
    left: 300px;
    top: 96px;
    width: 1.5px;
    height: 130px;
    background: linear-gradient(to bottom, rgba(255,255,255,0), rgba(255,255,255,0.85) 50%, rgba(255,255,255,0));
  }
  .contact {
    position: absolute;
    left: 320px;
    top: 150px;
    font-size: 14px;
    line-height: 1.35;
    list-style: none;
  }
  .contact__item {
    display: flex;
    align-items: flex-start;
    gap: 10px;
    margin-bottom: 10px;
  }
  .contact__icon { width: 18px; height: 18px; flex: none; margin-top: 1px; }

  .card--back .ghost-brand {
    position: absolute;
    right: 28px;
    top: 26px;
    font-size: 13px;
    color: var(--ink-faint);
    letter-spacing: 0.04em;
  }
  .back-swirl {
    position: absolute;
    left: 30px;
    bottom: 20px;
    width: 180px;
    height: 140px;
    border-radius: 50%;
    background: radial-gradient(ellipse at center, rgba(60,60,60,0.35) 0%, rgba(0,0,0,0) 70%);
  }
  .appointment-slip {
    position: absolute;
    left: 140px;
    top: 72px;
    width: 290px;
    height: 150px;
    background: var(--slip);
    padding: 34px 22px 0 22px;
  }
  .appointment-slip__line {
    height: 1px;
    background: var(--slip-rule);
    margin-bottom: 38px;
  }
</style>
</head>
<body>
  <section class="card card--front" aria-label="Business card front">
    <div class="swirl-art" role="img" aria-label="Soft decorative swirl"></div>
    <div class="brand"><span class="brand__dot"></span>Vintner Dental</div>
    <div class="identity">
      <h1 class="identity__name">Dr Marlo Vintner</h1>
      <p class="identity__title">Doctor of Dental Medicine</p>
    </div>
    <div class="divider"></div>
    <ul class="contact">
      <li class="contact__item">
        <svg class="contact__icon" viewBox="0 0 24 24" fill="none" stroke="#fff" stroke-width="1.6">
          <path d="M12 21s-6-6.2-6-11a6 6 0 0 1 12 0c0 4.8-6 11-6 11z"/>
          <circle cx="12" cy="10" r="2.4"/>
        </svg>
        <span>5182 Ch. Birchfield<br>Montreal QC H2T 4B9</span>
      </li>
      <li class="contact__item">
        <svg class="contact__icon" viewBox="0 0 24 24" fill="none" stroke="#fff" stroke-width="1.6">
          <circle cx="12" cy="12" r="9.5"/>
          <path d="M9.2 8.2c-.6.6-.5 2 .9 3.8s3 2.6 3.8 2.1l.9-.9-1.3-1.3-.8.5c-.6-.3-1.6-1.3-1.9-1.9l.5-.8-1.3-1.3z" fill="#fff" stroke="none"/>
        </svg>
        <span>514-629-5074</span>
      </li>
    </ul>
  </section>

  <section class="card card--back" aria-label="Business card back">
    <div class="back-swirl" role="img" aria-label="Soft decorative swirl"></div>
    <span class="ghost-brand">Vintner Dental</span>
    <div class="appointment-slip" aria-label="Next appointment">
      <div class="appointment-slip__line"></div>
      <div class="appointment-slip__line"></div>
      <div class="appointment-slip__line"></div>
    </div>
  </section>
</body>
</html>
```